New webpage design for development bureau

We are a development bureau in Denmark, and need a design for our webpage. We are called Harbor Development (Part of Harbor Fjeld Skolium Group), and are going to aim for multiple markets: Web, Apps, Desktop applications, ect.

We already have a logo, see the uploaded file. We do not have any special demands, other than in have to be simple. A portfolio view should also be available, for future customers.

```html
<!DOCTYPE html>
<html lang="en">
<head>
<meta charset="utf-8">
<title>Harbor Development</title>
<link rel="stylesheet" href="https://fonts.googleapis.com/css2?family=Source+Sans+3:wght@400;600;700&display=swap">
<style>
:root{
  --red:#e02b27;
  --tile:#f0574e;
  --ink:#1e1e1e;
  --text:#444;
  --grey-band:#ececec;
  --dark:#1b1b1b;
  --bar:#4a4a4a;
  --white:#fff;
}
*{margin:0;padding:0;box-sizing:border-box}
html,body{width:1200px;height:2507px;overflow:hidden}
body{position:relative;background:var(--white);font-family:"Source Sans 3",Arial,sans-serif;color:var(--ink)}
.abs{position:absolute}

/* header */
.site-header{left:0;top:0;width:1200px;height:97px;background:var(--white)}
.brand{left:162px;top:28px;font-size:36px;font-weight:700;letter-spacing:1px;color:var(--ink)}
.main-nav{right:185px;top:38px;display:flex;align-items:center;gap:14px;font-size:14px;font-weight:600;color:var(--ink)}
.main-nav .dot{width:5px;height:5px;border-radius:50%;background:var(--ink)}
.main-nav .active{color:var(--red)}

/* hero */
.hero{left:0;top:97px;width:1200px;height:506px;background:linear-gradient(100deg,#e9eef1 0%,#d5dde3 35%,#6f9fcc 55%,#cfe0ea 75%,#e6ebee 100%)}
.hero-arrow{top:302px;width:22px;height:26px;background:var(--red)}
.hero-arrow.prev{left:0}
.hero-arrow.next{right:0}

/* services */
.service{top:648px;width:300px;text-align:center}
.service-icon{width:64px;height:64px;border-radius:50%;background:var(--red);margin:0 auto;display:flex;align-items:center;justify-content:center}
.service h3{margin-top:22px;font-size:20px;font-weight:600}
.service p{margin-top:8px;font-size:12.5px;line-height:19px;color:var(--text)}

/* about */
.about-band{left:0;top:866px;width:1200px;height:287px;background:var(--grey-band)}
.section-title{width:1200px;left:0;text-align:center;font-size:31px;font-weight:400;color:var(--ink)}
.about-photo{left:214px;top:958px;width:166px;height:125px;background:linear-gradient(135deg,#f2f4f6,#c9d5e0 60%,#8aa4bf)}
.about-text{left:422px;top:961px;width:578px;font-size:12.2px;line-height:19px;color:var(--text);text-align:justify}

/* testimonials */
.quote-photo{left:216px;top:1257px;width:70px;height:60px;background:linear-gradient(135deg,#e6e6e6,#8a8f96 60%,#3e434a)}
.quote-mark{font-size:26px;font-weight:700;line-height:1;color:var(--ink)}
.quote-open{left:303px;top:1250px}
.quote-text{left:320px;top:1260px;width:680px;font-size:12.2px;line-height:19px;color:var(--text)}
.quote-author{left:320px;top:1318px;font-size:12.2px;color:var(--red)}

/* portfolio */
.portfolio{left:0;top:1383px;width:1200px;height:682px;background:var(--red);color:var(--white)}
.portfolio-title{left:0;top:1435px;width:1200px;text-align:center;font-size:31px;font-weight:400;color:var(--white)}
.portfolio-sub{left:0;top:1473px;width:1200px;text-align:center;font-size:16.5px;color:var(--white)}
.portfolio-rule{left:580px;top:1505px;width:40px;height:4px;background:var(--white)}
.grid{left:160px;top:1550px;width:880px;height:434px;display:grid;grid-template-columns:repeat(4,220px);grid-template-rows:repeat(2,217px)}
.tile{background:var(--tile);display:flex;flex-direction:column;align-items:center;justify-content:center;text-align:center;color:var(--white)}
.tile svg{margin-bottom:14px}
.tile .name{font-size:22px;font-weight:700;line-height:1}
.tile .kind{font-size:13px;font-weight:700;margin-top:2px}
.shot-a{background:linear-gradient(180deg,#23252e,#5a2a2e 50%,#2c2f38)}
.shot-b{background:linear-gradient(160deg,#f0f0f0,#c23a2c 40%,#e8e8e8 70%,#bfc3c8)}
.shot-c{background:linear-gradient(180deg,#2f5f9e,#f3f5f8 30%,#e8edf3)}
.shot-d{background:linear-gradient(180deg,#c5323a,#ede3da 35%,#d2c3b4)}

/* footer */
.footer{left:0;top:2065px;width:1200px;height:385px;background:var(--dark)}
.footer-title{left:0;top:2125px;width:1200px;text-align:center;font-size:24px;font-weight:700;color:var(--white)}
.social{top:2175px;width:40px;height:40px;border:1px solid #8a8a8a}
.social.first{border-color:var(--red)}
.newsletter-note{left:0;top:2246px;width:1200px;text-align:center;font-size:11.5px;font-weight:600;color:#e6e6e6}
.email-field{left:307px;top:2288px;width:586px;height:46px;background:#4a4a4a;color:#ddd;font-size:11.5px;font-weight:600;padding:17px 0 0 18px}
.subscribe{left:535px;top:2358px;width:130px;height:44px;border:1px solid #9a9a9a;color:var(--white);font-size:16px;font-weight:700;text-align:center;line-height:42px}
.bottom-bar{left:0;top:2450px;width:1200px;height:57px;background:var(--bar);color:#e6e6e6;font-size:11.5px;text-align:center;line-height:57px}
</style>
</head>
<body>

<header class="site-header abs">
  <div class="brand abs">HARBOR</div>
  <nav class="main-nav abs">
    <span class="active">Home</span><span class="dot"></span>
    <span>About Us</span><span class="dot"></span>
    <span>Services</span><span class="dot"></span>
    <span>Our Portfolio</span><span class="dot"></span>
    <span>Testimonials</span><span class="dot"></span>
    <span>Contact Us</span>
  </nav>
</header>

<section class="hero abs" role="img" aria-label="Hands working on a laptop with a glowing digital world map overlay"></section>
<div class="hero-arrow prev abs"><svg width="22" height="26" viewBox="0 0 22 26"><path d="M13 8l-5 5 5 5" stroke="#fff" stroke-width="2" fill="none"/></svg></div>
<div class="hero-arrow next abs"><svg width="22" height="26" viewBox="0 0 22 26"><path d="M9 8l5 5-5 5" stroke="#fff" stroke-width="2" fill="none"/></svg></div>

<div class="service abs" style="left:147px">
  <div class="service-icon"><svg width="34" height="30" viewBox="0 0 34 30"><rect x="3" y="3" width="28" height="19" fill="none" stroke="#fff" stroke-width="2.5"/><path d="M12 27h10M17 22v5M11 17l10-9" stroke="#fff" stroke-width="2.5"/></svg></div>
  <h3>Web Design</h3>
  <p>Lorem Ipsum is simply dummy text of the<br>printing and typesetting industry.<br>standard dummy text ever</p>
</div>
<div class="service abs" style="left:447px">
  <div class="service-icon"><svg width="24" height="34" viewBox="0 0 24 34"><rect x="3" y="2" width="18" height="30" rx="3" fill="none" stroke="#fff" stroke-width="2.5"/><circle cx="12" cy="27" r="1.8" fill="#fff"/></svg></div>
  <h3>App Applications</h3>
  <p>Lorem Ipsum is simply dummy text of the<br>printing and typesetting industry.<br>standard dummy text ever</p>
</div>
<div class="service abs" style="left:740px">
  <div class="service-icon"><svg width="34" height="30" viewBox="0 0 34 30"><rect x="3" y="3" width="28" height="19" fill="none" stroke="#fff" stroke-width="2.5"/><path d="M12 27h10M17 22v5" stroke="#fff" stroke-width="2.5"/></svg></div>
  <h3>Desktop applications</h3>
  <p>Lorem Ipsum is simply dummy text of the<br>printing and typesetting industry. standard<br>dummy text ever</p>
</div>

<section class="about-band abs"></section>
<h2 class="section-title abs" style="top:888px">About Harbor</h2>
<div class="about-photo abs" role="img" aria-label="Portrait of a smiling businessman in a light office"></div>
<p class="about-text abs">Vestibulum sit amet neque eu neque suscipit consequat quis vel risus. Vestibulum vehicula purus nec dui accumsan fermentum. Suspendisse potenti. Ut dapibus est id odio pretium blandit in eget leo.Vestibulum sit amet neque eu neque suscipit consequat quis vel risus. Vestibulum vehicula purus nec dui accumsan fermentum. Suspendisse potenti. Ut dapibus est id odio pretium blandit in eget leo.Vestibulum sit amet neque eu neque suscipit consequat quis vel risus. Vestibulum vehicula purus nec dui accumsan fermentum. Suspendisse potenti. Ut dapibus est id odio pretium blandit in eget leo.Vestibulum sit amet neque eu neque suscipit consequat quis vel risus. Vestibulum vehicula purus nec dui accumsan fermentum.</p>

<h2 class="section-title abs" style="top:1188px">Testimonials</h2>
<div class="quote-photo abs" role="img" aria-label="Portrait of a client in a suit"></div>
<div class="quote-mark quote-open abs">&ldquo;</div>
<p class="quote-text abs">Vestibulum sit amet neque eu neque suscipit consequat quis vel risus. Vestibulum vehicula purus nec dui accumsan fermentum. Suspendisse potenti. Ut dapibus est id odio pretium blandit in eget leo.Vestibulum sit amet neque eu neque suscipit consequat quis vel risus. Vestibulum dui accumsan fermentum. <b class="quote-mark" style="font-size:18px">&rdquo;</b></p>
<div class="quote-author abs">- Mark Holm</div>

<section class="portfolio abs"></section>
<h2 class="portfolio-title abs">Our Portfolio</h2>
<div class="portfolio-sub abs">We are added our featured works below</div>
<div class="portfolio-rule abs"></div>
<div class="grid abs">
  <div class="tile"><svg width="32" height="28" viewBox="0 0 32 28"><path d="M2 14L30 2 22 26 15 17z M15 17L30 2" fill="none" stroke="#fff" stroke-width="1.8" stroke-linejoin="round" opacity=".8"/></svg><div class="name">Project Name</div><div class="kind">Business marketing</div></div>
  <div class="shot-a" role="img" aria-label="Website screenshot of a dark business template"></div>
  <div class="tile"><svg width="32" height="28" viewBox="0 0 32 28"><path d="M2 14L30 2 22 26 15 17z M15 17L30 2" fill="none" stroke="#fff" stroke-width="1.8" stroke-linejoin="round" opacity=".8"/></svg><div class="name">Project Name</div><div class="kind">Landing page</div></div>
  <div class="shot-b" role="img" aria-label="Website screenshot of a car rental template"></div>
  <div class="shot-c" role="img" aria-label="Website screenshot of a blue corporate portal"></div>
  <div class="tile"><svg width="32" height="28" viewBox="0 0 32 28"><path d="M2 14L30 2 22 26 15 17z M15 17L30 2" fill="none" stroke="#fff" stroke-width="1.8" stroke-linejoin="round" opacity=".8"/></svg><div class="name">Project Name</div><div class="kind">Landing page</div></div>
  <div class="shot-d" role="img" aria-label="Website screenshot of a restaurant template"></div>
  <div class="tile"><svg width="32" height="28" viewBox="0 0 32 28"><path d="M2 14L30 2 22 26 15 17z M15 17L30 2" fill="none" stroke="#fff" stroke-width="1.8" stroke-linejoin="round" opacity=".8"/></svg><div class="name">Project Name</div><div class="kind">Restaurant Page</div></div>
</div>

<footer class="footer abs"></footer>
<h2 class="footer-title abs">Get in touch</h2>
<div class="social first abs" style="left:490px" aria-label="Social profile"></div>
<div class="social abs" style="left:549px" aria-label="Social profile"></div>
<div class="social abs" style="left:608px" aria-label="Social profile"></div>
<div class="social abs" style="left:667px" aria-label="Social profile"></div>
<div class="newsletter-note abs">Subscribe to our newsletter to stay update with what is new</div>
<div class="email-field abs">Email Address</div>
<div class="subscribe abs">Subscribe</div>
<div class="bottom-bar abs">harbordev.dk &copy; 2014 All Rights Reserved</div>

</body>
</html>
```